Premium CBD/Hemp company needs packaging and label design

Verdant Oakfield, a premium CBD/Hemp company based in Scottsdale, Arizona is in need of a packaging and label design. We are launching with our flagship product which will be a 30 count capsule and will come in three functions: Pain Relief, Anxiety Support, and Sleep Support. For the purpose of this contest, please design packaging and label for our Anxiety Support product. Our products are physician formulated and all natural. Our main ingredient is CBD/Hemp and is complemented by specific herbs that synergistically work together to give the customer the most effective and desired result. We would like our branding to have a pharmaceutical look and feel with a focus on trust and transparency. We have uploaded our company logo that is to be used on both the packaging and label. We have also uploaded an executed branding questionnaire that will guide you to exactly what we are seeking to achieve as to the look and feel of our brand. Please feel free to contact us with any questions that you may have. The winner of this contest will have the opportunity to work with us on future projects as we will need packaging and label design for our entire Verdant Oakfield product line.

Target Market(s)

See attached branding questionnaire

Industry/Entity Type

Health And Wellness

Font styles to use
Sans Serif

Colors

Designer to choose colors to be used in the design.

Requirements
Must have
• See attached branding questionnaire; Please superimpose labels onto a cobalt blue capsule bottle (see attached)
• >>UPON REVIEW of the FIRST 8 designs, we really like the silver, mildly metallic label background in DESIGN # 21300528, we do not want metalic lettering as that would not look very "Pharmaceutical"
• >>We are in search of a look that is a bit more "Pharmaceutical" than a look that would be more commonly found in a Supplement Store
Nice to have
• "See attached branding questionnaire
Should not have
• See attached branding questionnaire; NO marijuana or cannabis plant on the packaging or label

```html
<!DOCTYPE html>
<html lang="en">
<head>
<meta charset="utf-8">
<title>Verdant Oakfield — Hemp Extract Anxiety Support Packaging</title>
<link rel="stylesheet" href="https://fonts.googleapis.com/css2?family=Dosis:wght@400;500;600;700;800&display=swap">
<style>
  :root {
    --stage: #6f7b7e;
    --stage-light: #a9b2b3;
    --green: #1f8a45;
    --green-deep: #1a6e39;
    --green-tag: #1c5c33;
    --cobalt: #2b3b95;
    --silver: #eeeff0;
    --silver-shade: #dcdedf;
    --ink-light: #e8ebe9;
    --ink-soft: #cfd8d2;
  }
  * { box-sizing: border-box; margin: 0; padding: 0; }
  html, body { width: 1200px; height: 1200px; overflow: hidden; }
  body {
    background: radial-gradient(circle at 55% 40%, var(--stage-light) 0%, var(--stage) 65%);
    font-family: "Dosis", sans-serif;
    position: relative;
  }

  /* ---------- Carton (flattened side + front panel) ---------- */
  .carton { position: absolute; left: 110px; top: 140px; width: 540px; height: 920px; display: flex; }
  .carton-side {
    width: 230px; height: 100%;
    background: linear-gradient(180deg, var(--silver) 0%, var(--silver-shade) 100%);
    position: relative;
  }
  .carton-front { width: 310px; height: 100%; position: relative; background: var(--green); }

  .brand-vertical {
    position: absolute; left: 50%; top: 50%;
    transform: translate(-50%, -50%) rotate(-90deg);
    display: flex; align-items: center; gap: 14px; white-space: nowrap;
  }
  .brand-dot { width: 26px; height: 26px; border-radius: 50%; background: var(--cobalt); flex: none; }
  .brand-name { color: var(--cobalt); font-weight: 600; letter-spacing: 3px; text-transform: uppercase; }
  .carton .brand-name { font-size: 40px; }

  .edge-stripe { position: absolute; left: 0; top: 0; bottom: 0; width: 16px; background: var(--cobalt); }
  .pattern-field { position: absolute; inset: 0; background: linear-gradient(180deg, var(--green) 0%, var(--green-deep) 100%); }

  .spectrum-band {
    position: absolute; left: 0; right: 0;
    background: var(--cobalt); color: var(--ink-light);
    font-weight: 600; text-transform: uppercase; text-align: center;
    display: flex; align-items: center; justify-content: center;
  }
  .title-hemp { position: absolute; left: 0; right: 0; text-align: center; color: var(--ink-light); font-weight: 800; line-height: 1; }
  .title-extract { position: absolute; left: 0; right: 0; text-align: center; color: var(--ink-light); font-weight: 400; line-height: 1; letter-spacing: 2px; }
  .rule { position: absolute; height: 3px; background: var(--cobalt); }
  .function-name { position: absolute; left: 0; right: 0; text-align: center; color: var(--ink-soft); font-weight: 600; text-transform: uppercase; line-height: 1; }
  .tag-natural {
    position: absolute; left: 50%; transform: translateX(-50%);
    background: var(--green-tag); color: var(--ink-light);
    font-weight: 700; text-transform: uppercase; white-space: nowrap;
    display: flex; align-items: center; justify-content: center;
  }
  .supplement-note { position: absolute; left: 0; right: 0; text-align: center; color: var(--ink-light); font-weight: 600; text-transform: uppercase; }
  .count-pill {
    position: absolute; left: 50%; transform: translateX(-50%);
    display: flex; border: 2px solid var(--cobalt); border-radius: 999px; overflow: hidden;
    font-weight: 600; text-transform: uppercase; white-space: nowrap;
  }
  .count-pill .count { background: var(--cobalt); color: var(--ink-light); display: flex; align-items: center; }
  .count-pill .dose { color: #5fbf7d; display: flex; align-items: center; }

  /* carton front sizes */
  .carton-front .spectrum-band { top: 198px; height: 57px; font-size: 26px; padding-left: 16px; }
  .carton-front .title-hemp { top: 388px; font-size: 76px; padding-left: 16px; }
  .carton-front .title-extract { top: 470px; font-size: 38px; padding-left: 16px; }
  .carton-front .rule-top { top: 530px; left: 80px; right: 20px; }
  .carton-front .rule-bottom { top: 578px; left: 80px; right: 20px; }
  .carton-front .function-name { top: 540px; font-size: 25px; padding-left: 16px; }
  .carton-front .tag-natural { top: 584px; height: 26px; padding: 0 10px; font-size: 15px; margin-left: 8px; }
  .carton-front .supplement-note { top: 838px; font-size: 13px; padding-left: 16px; }
  .carton-front .count-pill { top: 858px; height: 30px; margin-left: 8px; }
  .carton-front .count-pill .count { padding: 0 10px; font-size: 12px; }
  .carton-front .count-pill .dose { padding: 0 14px; font-size: 14px; }

  /* ---------- Bottle label (flattened) ---------- */
  .label { position: absolute; left: 700px; top: 360px; width: 410px; height: 530px; display: flex; }
  .label-side { width: 78px; height: 100%; background: linear-gradient(180deg, var(--silver) 0%, var(--silver-shade) 100%); position: relative; }
  .label .brand-name { font-size: 22px; letter-spacing: 2px; }
  .label .brand-dot { width: 16px; height: 16px; }
  .label .brand-vertical { top: 68%; gap: 10px; }
  .label-main { flex: 1; position: relative; background: var(--green); }
  .label-main .edge-stripe { width: 10px; }
  .label-main .spectrum-band { top: 110px; height: 24px; font-size: 18px; padding-left: 10px; }
  .label-main .title-hemp { top: 150px; font-size: 78px; padding-left: 10px; }
  .label-main .title-extract { top: 222px; font-size: 42px; padding-left: 10px; }
  .label-main .rule-top { top: 337px; left: 50px; right: 30px; }
  .label-main .rule-bottom { top: 380px; left: 50px; right: 30px; }
  .label-main .function-name { top: 348px; font-size: 24px; padding-left: 10px; }
  .label-main .tag-natural { top: 389px; height: 22px; padding: 0 10px; font-size: 14px; margin-left: 5px; }
  .label-main .supplement-note { top: 482px; font-size: 11px; padding-left: 10px; }
  .label-main .count-pill { top: 500px; height: 22px; margin-left: 5px; }
  .label-main .count-pill .count { padding: 0 7px; font-size: 9px; }
  .label-main .count-pill .dose { padding: 0 12px; font-size: 11px; }
</style>
</head>
<body>

<section class="carton" aria-label="Carton, side and front panels">
  <div class="carton-side">
    <div class="brand-vertical">
      <span class="brand-dot"></span>
      <span class="brand-name">Verdant Oakfield</span>
    </div>
  </div>
  <div class="carton-front">
    <div class="pattern-field" role="img" aria-label="Green field with a faint repeating pattern of circular leaf motifs"></div>
    <div class="edge-stripe"></div>
    <div class="spectrum-band">Full Spectrum</div>
    <h1 class="title-hemp">HEMP</h1>
    <p class="title-extract">EXTRACT</p>
    <div class="rule rule-top"></div>
    <p class="function-name">Anxiety Support</p>
    <div class="rule rule-bottom"></div>
    <p class="tag-natural">All Natural</p>
    <p class="supplement-note">Dietary Supplement</p>
    <div class="count-pill"><span class="count">30 Capsules</span><span class="dose">25mg</span></div>
  </div>
</section>

<section class="label" aria-label="Bottle label, flattened">
  <div class="label-side">
    <div class="brand-vertical">
      <span class="brand-dot"></span>
      <span class="brand-name">Verdant Oakfield</span>
    </div>
  </div>
  <div class="label-main">
    <div class="pattern-field" role="img" aria-label="Green field with a faint repeating pattern of circular leaf motifs"></div>
    <div class="edge-stripe"></div>
    <div class="spectrum-band">Full Spectrum</div>
    <h2 class="title-hemp">HEMP</h2>
    <p class="title-extract">EXTRACT</p>
    <div class="rule rule-top"></div>
    <p class="function-name">Anxiety Support</p>
    <div class="rule rule-bottom"></div>
    <p class="tag-natural">All Natural</p>
    <p class="supplement-note">Dietary Supplement</p>
    <div class="count-pill"><span class="count">30 Capsules</span><span class="dose">25mg</span></div>
  </div>
</section>

</body>
</html>
```